Corporate flyer introducing a brand new technology apprenticeship program in Australia!

A professional, yet clean and contemporary looking flyer to advertise a brand new service offering in a simple, easy to read format with engaging images. Here is a link to our current online brochure which outlines the program we would like to advertise in a hardcopy flyer/brochure format: https://pages.brivento.com/Information-on-Technology-Higher-Apprenticeships-for-Employers-Victoria-kT3pzLw7QeRM

Target Market(s)

Medium to large sized businesses involved in using cutting edge technology, such as engineering and advanced manufracturing (3D printing etc)

Industry/Entity Type

Engineering

Colors

Designer to choose colors to be used in the design.

Requirements
Must have
• Contemporary, clean looking, easy to read, tech/engineering/advanced manufacturing related imagery
Nice to have
• Some ideas about different sizes/styles (eg something other than a plain A4 sheet)
Should not have
• Unprofessional or offensive language

```html
<!DOCTYPE html>
<html lang="en">
<head>
<meta charset="utf-8">
<title>Technology Higher Apprentices – 2019 Program</title>
<link rel="stylesheet" href="https://fonts.googleapis.com/css2?family=Josefin+Sans:wght@300;400;700&display=swap">
<style>
  :root {
    --canvas-bg: #e4e4e4;
    --band-orange: #e66d4b;
    --title-orange: #ee7a50;
    --ink-dark: #3a3f47;
    --white: #ffffff;
    --photo-blue: #8e9bb8;
    --photo-skin: #e8c4ae;
    --photo-light: #f4efe9;
    --photo-wood: #d7ab85;
  }
  * { box-sizing: border-box; margin: 0; padding: 0; }
  html, body {
    width: 1200px;
    height: 972px;
    overflow: hidden;
    background: var(--canvas-bg);
    font-family: "Josefin Sans", "Futura", sans-serif;
  }
  .cover {
    position: absolute;
    left: 130px;
    top: 116px;
    width: 940px;
    height: 740px;
    background: var(--white);
    box-shadow: 0 6px 18px rgba(0,0,0,0.12);
    overflow: hidden;
  }
  .cover-photo {
    position: absolute;
    inset: 0 0 170px 0;
    background:
      radial-gradient(ellipse 40% 35% at 62% 30%, rgba(255,255,255,0.9), transparent 70%),
      radial-gradient(ellipse 30% 25% at 45% 70%, var(--photo-skin), transparent 75%),
      radial-gradient(ellipse 25% 40% at 90% 55%, var(--photo-wood), transparent 75%),
      linear-gradient(100deg, var(--photo-blue) 0%, #b3bdd2 30%, var(--photo-light) 60%, #ead6c3 100%);
  }
  .cover-photo::after {
    content: "";
    position: absolute;
    inset: 0;
    background: linear-gradient(180deg, rgba(255,255,255,0.45) 0%, rgba(255,255,255,0) 55%);
  }
  .title-block {
    position: absolute;
    left: 350px;
    top: 70px;
    color: var(--title-orange);
  }
  .title {
    font-weight: 700;
    font-size: 60px;
    line-height: 0.98;
    letter-spacing: 7px;
    text-transform: uppercase;
  }
  .title span { display: block; }
  .title .line-2 { padding-left: 70px; }
  .title .line-3 { padding-left: 30px; }
  .edition {
    display: inline-block;
    margin: 16px 0 0 140px;
    padding: 10px 18px 6px;
    border: 2px solid var(--ink-dark);
    color: var(--ink-dark);
    font-size: 24px;
    font-weight: 400;
    letter-spacing: 6px;
    text-transform: uppercase;
    background: rgba(255,255,255,0.55);
  }
  .cover-band {
    position: absolute;
    left: 0; right: 0; bottom: 0;
    height: 170px;
    background: var(--band-orange);
    color: var(--white);
  }
  .tagline {
    position: absolute;
    left: 150px;
    top: 78px;
    width: 320px;
    font-weight: 300;
    font-size: 21px;
    line-height: 1.25;
  }
  .brand {
    position: absolute;
    right: 48px;
    top: 44px;
    display: flex;
    align-items: center;
    gap: 14px;
  }
  .brand-mark {
    width: 22px;
    height: 22px;
    background: var(--white);
  }
  .brand-name {
    font-weight: 700;
    font-size: 26px;
    letter-spacing: 1px;
    text-transform: uppercase;
    line-height: 1;
  }
</style>
</head>
<body>
  <main class="cover">
    <div class="cover-photo" role="img" aria-label="Photograph of hands typing on a laptop while a colleague points at the screen, soft office light"></div>

    <header class="title-block">
      <h1 class="title">
        <span class="line-1">Technology</span>
        <span class="line-2">Higher</span>
        <span class="line-3">Apprentices</span>
      </h1>
      <p class="edition">2019 Program</p>
    </header>

    <footer class="cover-band">
      <p class="tagline">The future is determined by the decisions you make today.</p>
      <div class="brand">
        <span class="brand-mark"></span>
        <span class="brand-name">Corvex Workforce</span>
      </div>
    </footer>
  </main>
</body>
</html>
```